Heron Trade finance web design

We are a newly established business which provides invoice finance to Small Businesses in England and Wales.
Our approach is very much a funder where the small business owner can talk to the decision maker. We will guarantee on receipt of information, a decision within 24 hours.
We are not a bank so the look of the website need to be friendly but professional.
Have two types of people we are trying to attract to the website: 1) partners who are small business owners and 2) introducers who is accountants and commercial brokers who introduce us to the small businesses.
Currently no website, although domain has been reserved.
The design should be:
Professional
“Clean” Look
Designed to convey Trust and Authority.
Appeal to the small business owner.
Must incorporate:
Logo (attached)
Front page:Top tabs to other pages 1) About us 2) Services 3) Introducers 4) Contact us
Need picture and logo on page.
1) About us page- Room for talk about the company, the people and our critera.
2) Services page- We need for what invoice finance is, and 5 boxes for different services we will provide. (link on page to contact us)
3) Introducers page- We need a part for why become an introducer? Who we can help? Why we are different? (link on page to contact us)
4) Contact us page- Office address, email, tel and if possible a map and a contact me part which will email direct to us.
Text will be provided for the design, if we can see the setup of the website we will provide a part for each of the pages to support.
Styles we think convey the correct image:
www.brindlecapital.example
www.tollmarkfs.example
www.qelfunding.example
Small business owners
Finance
5+ page

```html
<!DOCTYPE html>
<html lang="en">
<head>
<meta charset="utf-8">
<title>Heron Trade finance</title>
<link href="https://fonts.googleapis.com/css2?family=Open+Sans:ital,wght@0,300;0,400;0,600;1,400&display=swap" rel="stylesheet">
<style>
:root{
  --red:#b8121c;
  --red-dark:#9e0f17;
  --ink:#333;
  --muted:#666;
  --soft-bg:#f5f5f9;
  --white:#fff;
  --dark:#2a2a2a;
}
*{box-sizing:border-box;margin:0;padding:0}
html,body{width:1200px;height:2663px;overflow:hidden}
body{font-family:"Open Sans",Arial,sans-serif;color:var(--ink);background:var(--white);position:relative}
section,header,footer{position:absolute;left:0;width:1200px}
.abs{position:absolute}
.center{text-align:center;left:0;width:1200px}

/* header */
.site-header{top:0;height:92px;border-top:3px solid var(--red);background:var(--white);box-shadow:0 2px 6px rgba(0,0,0,.12);z-index:2}
.brand{left:133px;top:22px;display:flex;align-items:center;gap:10px;font-size:26px;font-weight:600;color:var(--red);white-space:nowrap}
.brand-dot{width:14px;height:14px;border-radius:50%;background:var(--red)}
.main-nav{right:133px;top:0;height:89px;display:flex;gap:44px;align-items:center}
.main-nav a{font-size:12.5px;color:var(--ink);text-decoration:none;height:89px;line-height:89px;position:relative}
.main-nav a.active{color:var(--red)}
.main-nav a.active::after{content:"";position:absolute;left:0;right:0;bottom:0;height:3px;background:var(--red)}

/* buttons */
.btn-solid{display:inline-block;background:var(--red);color:var(--white);font-weight:600;font-size:13px;border-radius:24px;text-align:center;text-decoration:none}
.btn-small{display:inline-block;width:96px;height:34px;line-height:32px;font-size:11.5px;border-radius:17px;text-align:center;text-decoration:none}
.btn-small.filled{background:var(--red);color:var(--white);border:1px solid var(--red)}
.btn-small.outline{border:1px solid #333;color:var(--ink)}

/* hero */
.hero{top:92px;height:458px}
.hero-photo{position:absolute;inset:0;background:linear-gradient(100deg,#5a5048 0%,#8a7a6a 30%,#6b6a6e 55%,#7d6955 80%,#4d4036 100%)}
.hero-shade{position:absolute;inset:0;background:rgba(0,0,0,.28)}
.hero-title{top:158px;font-size:56px;font-weight:300;color:var(--white)}
.hero-sub{top:250px;font-size:14.5px;color:var(--white)}
.hero .btn-solid{left:507px;top:298px;width:186px;height:46px;line-height:46px}
.dots{display:flex;gap:8px;justify-content:center}
.dots span{width:7px;height:7px;border-radius:50%;background:rgba(255,255,255,.5)}
.dots span.on{background:var(--white)}
.hero .dots{top:414px}

/* services */
.services{top:550px;height:476px}
.section-title{font-size:34px;font-weight:300;color:#444}
.services .section-title{top:38px}
.service{top:112px;width:266px;text-align:center}
.service-icon{width:103px;height:103px;border-radius:50%;margin:0 auto;display:flex;align-items:center;justify-content:center;background:#111}
.service-icon.red{background:var(--red)}
.service h3{margin-top:38px;font-size:20px;font-weight:400;color:#222}
.service p{margin-top:14px;font-size:12.5px;line-height:22px;color:var(--muted)}
.service .btn-small{margin-top:26px}

/* receivables */
.receivables{top:1026px;height:426px;background:var(--soft-bg)}
.receivables h2{left:133px;top:55px;font-size:33px;font-weight:300;color:#444}
.receivables .lead{left:133px;top:118px;width:470px;font-size:12.5px;font-style:italic;line-height:23px;color:var(--muted)}
.checklist{left:133px;top:174px;list-style:none}
.checklist li{font-size:13px;line-height:22.5px;color:var(--red);padding-left:22px;position:relative}
.checklist li::before{content:"›";position:absolute;left:2px;top:-1px;font-size:16px}
.receivables .btn-small{left:133px;top:294px;width:97px}
.monitor{left:685px;top:62px;width:383px;height:305px}

/* rates */
.rates{top:1452px;height:440px}
.rates-photo{position:absolute;inset:0;background:linear-gradient(110deg,#3d3d3d 0%,#6a6a68 35%,#4a4a4a 60%,#2b2b2b 100%)}
.rates-shade{position:absolute;inset:0;background:rgba(0,0,0,.35)}
.rates h2{top:106px;font-size:46px;font-weight:300;color:var(--white)}
.rates p{top:192px;left:220px;width:760px;text-align:center;font-size:12px;line-height:24px;color:#eee}
.rates .btn-solid{left:503px;top:268px;width:194px;height:42px;line-height:42px}

/* testimonial */
.testimonial{top:1892px;height:460px}
.testimonial .section-title{top:56px}
.avatar{left:544px;top:149px;width:112px;height:112px;border-radius:50%;background:radial-gradient(circle at 50% 40%,#b89a86,#6d6a6a 70%)}
.quote{left:133px;top:294px;width:934px;text-align:center;font-size:12.5px;line-height:23px;color:var(--muted)}
.author{top:360px;font-size:13px;font-style:italic;color:var(--red)}
.testimonial .dots{top:404px}
.testimonial .dots span{background:#bbb;width:8px;height:8px}
.testimonial .dots span.on{background:var(--red)}

/* footer */
.site-footer{top:2352px;height:311px;background:var(--red);color:var(--white)}
.foot-col{top:37px}
.foot-col h4{font-size:17px;font-weight:400;padding-bottom:14px;border-bottom:1px solid rgba(255,255,255,.18);width:190px}
.foot-col ul{list-style:none;margin-top:16px}
.foot-col li{font-size:11.5px;line-height:22.5px}
.social li{display:flex;align-items:center;gap:10px}
.social i{width:10px;height:10px;border-radius:50%;background:var(--white);display:inline-block}
.foot-rule{left:133px;top:250px;width:934px;height:1px;background:rgba(255,255,255,.18)}
.copyright{top:269px;font-size:11px;color:#f3d0d2}
</style>
</head>
<body>

<header class="site-header">
  <div class="abs brand"><span class="brand-dot"></span>Heron Trade finance</div>
  <nav class="abs main-nav">
    <a href="#" class="active">HOME</a>
    <a href="#">ABOUT US</a>
    <a href="#">SERVICES</a>
    <a href="#">INTRODUCERS</a>
    <a href="#">CONTACT US</a>
  </nav>
</header>

<section class="hero">
  <div class="hero-photo" role="img" aria-label="Photo of a small business team working together around a desk in a bright office"></div>
  <div class="hero-shade"></div>
  <h1 class="abs center hero-title">Finance to Small Businesses</h1>
  <p class="abs center hero-sub">We are a new business which provides invoice finance to Small Businesses in England and Wales.</p>
  <a href="#" class="abs btn-solid">GET STARTED NOW</a>
  <div class="abs center dots"><span class="on"></span><span></span><span></span></div>
</section>

<section class="services">
  <h2 class="abs center section-title">Our Services</h2>

  <div class="abs service" style="left:133px">
    <div class="service-icon red">
      <svg width="40" height="34" viewBox="0 0 40 34"><rect x="13" y="2" width="14" height="8" rx="2" fill="none" stroke="#fff" stroke-width="3"/><rect x="2" y="9" width="36" height="23" rx="3" fill="#fff"/><rect x="2" y="17" width="36" height="2" fill="#b8121c"/><rect x="17" y="15" width="6" height="6" fill="#fff" stroke="#b8121c" stroke-width="1.5"/></svg>
    </div>
    <h3>INVESTMENT</h3>
    <p>Neque porro quisquam est, qui dolorem ipsum quia dolor sit amet, consectetur, adipisci velit, sed quia non numquam eius modi</p>
    <a href="#" class="btn-small filled">Learn More</a>
  </div>

  <div class="abs service" style="left:467px">
    <div class="service-icon">
      <svg width="44" height="34" viewBox="0 0 44 34"><path d="M3 2v29h39" fill="none" stroke="#fff" stroke-width="3"/><path d="M7 28l9-14 7 8 7-12 10 18z" fill="#fff"/></svg>
    </div>
    <h3>STRATEGY</h3>
    <p>Neque porro quisquam est, qui dolorem ipsum quia dolor sit amet, consectetur, adipisci velit, sed quia non numquam eius modi</p>
    <a href="#" class="btn-small outline">Learn More</a>
  </div>

  <div class="abs service" style="left:801px">
    <div class="service-icon">
      <svg width="40" height="36" viewBox="0 0 40 36"><path d="M4 12h8l18-9v28l-18-9H4z" fill="#fff"/><path d="M10 22l4 12h5l-3-12z" fill="#fff"/><rect x="33" y="13" width="5" height="8" rx="2" fill="#fff"/></svg>
    </div>
    <h3>MARKETING</h3>
    <p>Neque porro quisquam est, qui dolorem ipsum quia dolor sit amet, consectetur, adipisci velit, sed quia non numquam eius modi</p>
    <a href="#" class="btn-small outline">Learn More</a>
  </div>
</section>

<section class="receivables">
  <h2 class="abs">Accounts Receivable Financing</h2>
  <p class="abs lead">No more shopping around. After signing up for a free account, you will receive up to 30 instant quotes from invoice factoring companies.</p>
  <ul class="abs checklist">
    <li>Lorem ipsum dolor sit amet, consectetur adipiscing elit</li>
    <li>But I must explain to you how all this mistaken idea of denouncing pleasure</li>
    <li>Ut enim ad minima veniam, quis nostrum exercitationem ullam corporis suscipit</li>
    <li>At vero eos et accusamus et iusto odio dignissimos ducimus</li>
  </ul>
  <a href="#" class="abs btn-small filled">Learn More</a>
  <div class="abs monitor" role="img" aria-label="Desktop monitor showing a finance dashboard with charts and figures">
    <svg width="383" height="305" viewBox="0 0 383 305">
      <rect x="0" y="0" width="383" height="222" rx="8" fill="#1c1c1c"/>
      <rect x="8" y="8" width="367" height="206" fill="#dfe3ea"/>
      <rect x="0" y="222" width="383" height="38" rx="4" fill="#d9d9db"/>
      <path d="M150 260h83l8 38h-99z" fill="#c6c6c8"/>
      <rect x="120" y="296" width="143" height="6" rx="3" fill="#bdbdbf"/>
    </svg>
  </div>
</section>

<section class="rates">
  <div class="rates-photo" role="img" aria-label="Photo of a desk with paperwork, a coffee cup and a phone"></div>
  <div class="rates-shade"></div>
  <h2 class="abs center">How are Factoring Rates Structured?</h2>
  <p class="abs">Did you know that there are several options invoice factoring companies use to structure their factoring rates? We feel that one of our most important jobs is making sure that you understand factoring perfectly</p>
  <a href="#" class="abs btn-solid">GET STARTED NOW</a>
</section>

<section class="testimonial">
  <h2 class="abs center section-title">Customer Testimonial</h2>
  <div class="abs avatar" role="img" aria-label="Portrait photo of the customer"></div>
  <p class="abs quote">Lorem ipsum dolor sit amet, consectetur adipiscing elit, sed do eiusmod tempor incididunt ut labore et dolore magna aliqua. Ut enim ad minim veniam, quis nostrud exercitation ullamco laboris nisi ut aliquip ex ea commodo consequat. Duis aute irure dolor in reprehenderit in voluptate velit esse cillum dolore eu fugiat nulla pariatur.</p>
  <p class="abs center author">- Sam Porter -</p>
  <div class="abs center dots"><span></span><span class="on"></span><span></span></div>
</section>

<footer class="site-footer">
  <div class="abs foot-col" style="left:133px">
    <h4>SITEMAP</h4>
    <ul><li>Home</li><li>About us</li><li>Services</li><li>Introducers</li><li>Contact us</li></ul>
  </div>
  <div class="abs foot-col" style="left:398px">
    <h4>INDUSTRIES</h4>
    <ul><li>Banking</li><li>Transportation</li><li>Oil and Gas</li><li>Medical</li><li>Construction</li></ul>
  </div>
  <div class="abs foot-col" style="left:646px">
    <h4>RESOURCES</h4>
    <ul><li>Blog</li><li>Calculators</li><li>Infographics</li><li>Factoring Companies</li><li>Integrations &amp; Add-ons</li></ul>
  </div>
  <div class="abs foot-col" style="left:891px">
    <h4>CONNECT</h4>
    <ul class="social"><li><i></i>Friendbook</li><li><i></i>Chirper</li><li><i></i>RSS</li></ul>
  </div>
  <div class="abs foot-rule"></div>
  <p class="abs center copyright">© 2016 Heron Trade finance. All rights reserved.</p>
</footer>

</body>
</html>
```